Official personalized stationery with official coat of arms

I am looking for custom stationery design such as US letter size (8.5 X 11 or 21.6cm X 27.9cm), email signature (email) and envelope for US letter size (standard envelope no. 10 or 10.5cm X 24.5cm). Inspired by my personal coat of arms and my postal address:

4186 rue des Tilleuls
Levis, Quebec, H2K 4P7
Canada

Ideally a discreet design based on the coat of arms of Lucien Morvan but inspired by my mother's original coat of arms.

Something golden and translucent, simple but tasteful, without overemphasizing the green color. The coat of arms should have green, but not the entire structure of the stationery.

I am also looking for a small official thank you card in half letter size.

The design must be with the Lucien Morvan coat of arms and not the full coat of arms

Target Market(s)

For official communication

Industry/Entity Type

Communication officiel et parlementaire

Font styles to use
Other font styles liked:
• J’aime bien l’écriture comme le logo de la maison Delorme la police pour écrire le nom Delorme

Requirements
Must have
• Simplicity and use the Lucien Morvan coat of arms and not the full coat of arms
Nice to have
• Official and royal appearance as it is an official heraldic title of the British crown
Should not have
• Email and website

```html
<!DOCTYPE html>
<html lang="fr">
<head>
<meta charset="utf-8">
<title>Papeterie officielle — Lucien Morvan</title>
<link rel="stylesheet" href="https://fonts.googleapis.com/css2?family=Barlow:wght@500;600&family=Cormorant+Garamond:wght@600&display=swap">
<style>
  :root {
    --green: #165a30;
    --gold: #c9a236;
    --paper: #ffffff;
    --backdrop: #bdbdbd;
    --edge: #e2e2e2;
    --shadow: rgba(0, 0, 0, 0.38);
    --sans: "Barlow", Arial, sans-serif;
    --serif: "Cormorant Garamond", Georgia, serif;
  }
  html, body {
    margin: 0;
    width: 1200px;
    height: 1200px;
    overflow: hidden;
    background: var(--backdrop);
  }
  .canvas { position: relative; width: 1200px; height: 1200px; }

  .letterhead {
    position: absolute; left: 55px; top: 66px;
    width: 824px; height: 1065px;
    background: var(--paper);
    box-shadow: 4px 6px 16px var(--shadow);
  }
  .letterhead__crest {
    position: absolute; left: 0; right: 0; top: 170px;
    display: flex; flex-direction: column; align-items: center; gap: 16px;
  }
  .crest-mark {
    width: 56px; height: 56px; border-radius: 50%;
    background: var(--green);
  }
  .crest-name {
    font-family: var(--serif); font-weight: 600;
    color: var(--green); font-size: 34px; letter-spacing: 1px;
    white-space: nowrap;
  }
  .letterhead__rule {
    position: absolute; left: 0; right: 0; top: 1015px;
    height: 10px; background: var(--gold);
  }
  .letterhead__footer {
    position: absolute; left: 117px; top: 1000px;
    width: 589px; height: 40px;
    background: var(--green); color: #fff;
    display: flex; align-items: center; justify-content: center; gap: 10px;
    font-family: var(--sans); font-weight: 500; font-size: 15px;
  }

  .envelope {
    position: absolute; left: 546px; width: 604px;
    background: var(--paper); overflow: hidden;
    box-sizing: border-box;
    border: 1px solid var(--edge);
    box-shadow: 6px 9px 16px var(--shadow);
  }
  .envelope--slim { top: 421px; height: 141px; }
  .envelope--tall { top: 607px; height: 302px; }
  .envelope__swoosh { position: absolute; left: 0; bottom: 0; width: 604px; }
  .envelope--slim .envelope__swoosh { height: 141px; }
  .envelope--tall .envelope__swoosh { height: 139px; }
  .envelope__crest {
    position: absolute; left: 30px; width: 130px;
    display: flex; flex-direction: column; align-items: center; gap: 8px;
  }
  .envelope--slim .envelope__crest { top: 36px; }
  .envelope--tall .envelope__crest { top: 72px; }
  .envelope__crest .crest-mark { width: 36px; height: 36px; }
  .envelope__crest .crest-name { font-size: 20px; }
  .address {
    position: absolute; left: 346px;
    display: flex; gap: 10px;
    color: #fff; font-family: var(--sans); font-weight: 600;
    font-size: 15px; line-height: 18px;
  }
  .envelope--slim .address { top: 42px; }
  .envelope--tall .address { top: 210px; }
  .pin { width: 10px; height: 14px; margin-top: 2px; flex: none; }
</style>
</head>
<body>
<main class="canvas">

  <section class="letterhead">
    <div class="letterhead__crest">
      <span class="crest-mark"></span>
      <span class="crest-name">Lucien Morvan</span>
    </div>
    <div class="letterhead__rule"></div>
    <div class="letterhead__footer">
      <svg class="pin" viewBox="0 0 10 14"><path d="M5 0a5 5 0 0 1 5 5c0 3.5-5 9-5 9S0 8.5 0 5a5 5 0 0 1 5-5z" fill="#fff"/><circle cx="5" cy="5" r="1.8" fill="var(--green)"/></svg>
      <span>4186 rue des Tilleuls Levis, Quebec, H2K 4P7, Canada</span>
    </div>
  </section>

  <section class="envelope envelope--slim">
    <svg class="envelope__swoosh" viewBox="0 0 483 113" preserveAspectRatio="none">
      <path d="M150 0C205 15 195 50 160 75C125 100 135 110 200 113H205C150 105 145 90 170 70C200 45 210 15 160 0Z" fill="var(--gold)"/>
      <path d="M160 0H483V113H205C150 105 145 90 170 70C200 45 210 15 160 0Z" fill="var(--green)"/>
    </svg>
    <div class="envelope__crest">
      <span class="crest-mark"></span>
      <span class="crest-name">Lucien Morvan</span>
    </div>
    <div class="address">
      <svg class="pin" viewBox="0 0 10 14"><path d="M5 0a5 5 0 0 1 5 5c0 3.5-5 9-5 9S0 8.5 0 5a5 5 0 0 1 5-5z" fill="#fff"/><circle cx="5" cy="5" r="1.8" fill="var(--green)"/></svg>
      <span>4186 rue des Tilleuls<br>Levis, Quebec, H2K 4P7<br>Canada</span>
    </div>
  </section>

  <section class="envelope envelope--tall">
    <svg class="envelope__swoosh" viewBox="0 0 483 113" preserveAspectRatio="none">
      <path d="M150 0C205 15 195 50 160 75C125 100 135 110 200 113H205C150 105 145 90 170 70C200 45 210 15 160 0Z" fill="var(--gold)"/>
      <path d="M160 0H483V113H205C150 105 145 90 170 70C200 45 210 15 160 0Z" fill="var(--green)"/>
    </svg>
    <div class="envelope__crest">
      <span class="crest-mark"></span>
      <span class="crest-name">Lucien Morvan</span>
    </div>
    <div class="address">
      <svg class="pin" viewBox="0 0 10 14"><path d="M5 0a5 5 0 0 1 5 5c0 3.5-5 9-5 9S0 8.5 0 5a5 5 0 0 1 5-5z" fill="#fff"/><circle cx="5" cy="5" r="1.8" fill="var(--green)"/></svg>
      <span>4186 rue des Tilleuls<br>Levis, Quebec, H2K 4P7<br>Canada</span>
    </div>
  </section>

</main>
</body>
</html>
```